BRV Online

We are a telemedicine based HIV treatment, prevention and hep c clinic looking to help make our online presence known.

Target Market(s)

Future patients. We want to this be informative and have stock images of all different types of people

Industry/Entity Type

Medical

Coding

Coded - Design and coding required

Requirements
Must have
• A Home Page, A page on PrEP, HIV treatment and Hep C. A box in the corner that says book now and a contact us page.

```html
<!DOCTYPE html>
<html lang="en">
<head>
<meta charset="utf-8">
<title>BRV Online — Confidential HIV &amp; Hepatitis C Care</title>
<link href="https://fonts.googleapis.com/css2?family=Inter:wght@400;500;600;700&family=Poppins:wght@400;600;800&display=swap" rel="stylesheet">
<style>
:root{
  --blue:#1a6fc4;
  --blue-dark:#0d4a82;
  --navy:#0b4578;
  --green:#5aa63a;
  --ink:#111;
  --muted:#6b6f76;
  --sky:#dbeefd;
  --sky-soft:#eaf5fe;
  --card-border:#e4e9ef;
  --icon-bg:#d7ecfb;
  --icon-green:#e4f3da;
}
*{box-sizing:border-box;margin:0;padding:0}
html,body{width:1200px;height:4651px;overflow:hidden}
body{font-family:"Inter",sans-serif;color:var(--ink);background:#fff;position:relative}
a{color:inherit;text-decoration:none}
.section{position:absolute;left:0;width:1200px}
.eyebrow{font-size:17px;font-weight:600;color:var(--blue);letter-spacing:.3px;text-transform:uppercase}
.heading{font-family:"Poppins",sans-serif;font-weight:400;font-size:42px;line-height:1.3;color:var(--ink)}
.heading b{font-weight:800}
.center{text-align:center}
.btn{display:inline-flex;align-items:center;gap:10px;border-radius:22px;color:#fff;font-size:16px;font-weight:500;padding:0 24px;height:40px}
.btn-green{background:var(--green)}
.btn-blue{background:var(--blue)}
.btn-grad{background:linear-gradient(90deg,var(--green),var(--blue))}

/* header */
.site-header{top:0;height:128px;background:#fff}
.brand{position:absolute;left:125px;top:30px;display:flex;align-items:center;gap:12px;font-family:"Inter",sans-serif;font-weight:700;font-size:24px;color:var(--navy)}
.brand-dot{width:46px;height:46px;border-radius:50%;background:var(--blue)}
.nav{position:absolute;left:429px;top:45px;display:flex;gap:36px;font-size:15px;font-weight:500}
.nav .active{color:var(--blue)}
.header-cta{position:absolute;left:930px;top:33px;width:144px;height:42px;justify-content:center}

/* hero */
.hero{top:128px;height:730px;background:var(--sky);overflow:hidden}
.hero-art{position:absolute;left:520px;top:0;width:680px;height:560px;background:linear-gradient(135deg,#d8ecf8,#b9dcef 60%,#8ec2df)}
.hero-fade{position:absolute;left:420px;top:0;width:200px;height:560px;background:linear-gradient(90deg,var(--sky),rgba(219,238,253,0))}
.badge{position:absolute;left:125px;top:120px;background:#cfe6fb;border-radius:20px;padding:10px 28px;font-size:14px;color:var(--blue)}
.hero h1{position:absolute;left:125px;top:173px;font-family:"Poppins",sans-serif;font-weight:800;font-size:44px;line-height:1.25}
.hero h1 span{color:var(--blue)}
.hero p{position:absolute;left:125px;top:320px;width:490px;font-size:15px;line-height:1.4}
.hero .actions{position:absolute;left:125px;top:397px;display:flex;gap:24px}
.hero-curve{position:absolute;left:0;top:470px}

/* services */
.services{top:858px;height:720px;background:#f4f6fa}
.services .eyebrow{position:absolute;top:108px;width:100%}
.services .heading{position:absolute;top:150px;width:100%}
.card-row{position:absolute;top:266px;left:125px;display:flex;gap:17px}
.svc-card{width:306px;height:306px;background:#fff;border:1px solid var(--card-border);border-radius:8px;padding:22px;box-shadow:0 4px 14px rgba(0,0,0,.05)}
.svc-card.featured{border-color:#a8d39a}
.icon-circ{width:74px;height:74px;border-radius:50%;background:var(--icon-bg);display:flex;align-items:center;justify-content:center}
.svc-card.featured .icon-circ{background:var(--icon-green)}
.svc-card h3{font-size:17px;font-weight:700;margin:30px 0 18px}
.svc-card p{font-size:13.5px;line-height:1.55;color:var(--muted)}
.svc-card .more{display:flex;align-items:center;gap:8px;margin-top:12px;font-size:13.5px;font-weight:600;color:var(--blue)}
.svc-card.featured .more{color:var(--green)}

/* why */
.why{top:1578px;height:560px;background:var(--sky)}
.why-art{position:absolute;left:560px;top:0;width:640px;height:560px;background:linear-gradient(135deg,#cfe7f7,#a9d3ec)}
.why .eyebrow{position:absolute;left:125px;top:95px}
.why .heading{position:absolute;left:125px;top:125px;font-size:44px;line-height:1.1}
.checks{position:absolute;left:125px;top:270px;list-style:none}
.checks li{display:flex;align-items:center;gap:22px;font-size:18px;height:37.5px}

/* steps */
.steps{top:2138px;height:712px;background:#fff}
.steps .eyebrow{position:absolute;top:134px;width:100%}
.steps .heading{position:absolute;top:172px;width:100%}
.step-row{position:absolute;left:125px;top:292px;display:flex;gap:17px}
.step{position:relative;width:223px;height:296px;background:#fff;border:1px solid var(--card-border);border-radius:8px;padding:22px;box-shadow:0 4px 14px rgba(0,0,0,.05)}
.step .num{position:absolute;right:18px;top:10px;font-family:"Poppins",sans-serif;font-size:38px;font-weight:600;color:#d9dde2}
.step .icon-circ{background:var(--icon-green);width:72px;height:72px}
.step h3{font-size:17px;font-weight:700;margin:28px 0 20px;line-height:1.3;min-height:44px}
.step p{font-size:13.5px;line-height:1.55;color:var(--muted)}

/* stories */
.stories{top:2850px;height:630px;background:linear-gradient(180deg,#e3f1fc,#f1f8fe)}
.stories .eyebrow{position:absolute;top:62px;width:100%}
.stories .heading{position:absolute;top:100px;width:100%;text-transform:uppercase}
.story-row{position:absolute;left:125px;top:267px;display:flex;gap:17px}
.story{width:306px;height:262px;background:#fff;border:1px solid var(--card-border);border-radius:8px;padding:26px 18px}
.stars{color:#f2b70a;font-size:18px;letter-spacing:5px}
.story q{display:block;margin-top:18px;font-size:15.5px;line-height:1.5;quotes:none}
.person{display:flex;align-items:center;gap:14px;margin-top:26px}
.avatar{width:56px;height:56px;border-radius:50%;background:#c9d4de}
.person strong{font-size:15px;font-weight:600;display:block}
.person small{font-size:12px;color:var(--muted)}

/* cta */
.cta{top:3480px;height:700px;background:#f4f6fa}
.cta .eyebrow{position:absolute;top:138px;width:100%}
.cta .heading{position:absolute;top:180px;width:100%;text-transform:uppercase}
.cta p{position:absolute;top:318px;left:350px;width:500px;font-size:16px;line-height:1.3}
.cta .btn{position:absolute;top:384px;left:528px;width:144px;height:42px;justify-content:center}
.footer-curve{position:absolute;left:0;top:520px}

/* footer */
.site-footer{top:4180px;height:471px;background:var(--navy);color:#fff}
.foot-brand{position:absolute;left:100px;top:176px;display:flex;align-items:center;gap:12px;font-size:24px;font-weight:700}
.foot-brand .brand-dot{background:#fff}
.foot-col{position:absolute;top:84px}
.foot-col h4{font-size:17px;font-weight:600;margin-bottom:28px}
.foot-col ul{list-style:none}
.foot-col li{display:flex;align-items:center;gap:16px;font-size:16px;height:38px}
.dot-tick{width:16px;height:16px;border-radius:50%;background:var(--green);display:flex;align-items:center;justify-content:center}
.foot-rule{position:absolute;left:125px;top:388px;width:950px;height:1px;background:rgba(255,255,255,.25)}
.copyright{position:absolute;top:420px;width:100%;text-align:center;font-size:14px}
</style>
</head>
<body>

<header class="section site-header">
  <a class="brand" href="#"><span class="brand-dot"></span>BRV Online</a>
  <nav class="nav">
    <a class="active" href="#">Home</a><a href="#">PrEP</a><a href="#">HIV Treatment</a><a href="#">Hep C</a><a href="#">Contact Us</a>
  </nav>
  <a class="btn btn-grad header-cta" href="#">Book Now</a>
</header>

<section class="section hero">
  <div class="hero-art" role="img" aria-label="Patient on a video call with a doctor on a desktop monitor, with health chart graphics"></div>
  <div class="hero-fade"></div>
  <span class="badge">Secure Online Healthcare</span>
  <h1>Confidential Online<br><span>HIV &amp; Hepatitis</span> C Care</h1>
  <p>Fast, private telemedicine appointments for HIV treatment, PrEP, and Hepatitis C care—all from the comfort of your home.</p>
  <div class="actions">
    <a class="btn btn-green" href="#">Book Appointment <svg width="18" height="10" viewBox="0 0 18 10"><path d="M0 5h16M12 1l4 4-4 4" stroke="#fff" stroke-width="1.6" fill="none"/></svg></a>
    <a class="btn btn-blue" href="#">Learn More <svg width="18" height="10" viewBox="0 0 18 10"><path d="M0 5h16M12 1l4 4-4 4" stroke="#fff" stroke-width="1.6" fill="none"/></svg></a>
  </div>
  <svg class="hero-curve" width="1200" height="260" viewBox="0 0 1200 260">
    <path d="M0 80 Q300 -10 600 210 Q900 -10 1200 80 V260 H0Z" fill="#f4f6fa"/>
    <path d="M120 170 Q380 260 600 235 Q820 260 1080 170 Q820 225 600 215 Q380 225 120 170Z" fill="var(--blue)"/>
    <circle cx="600" cy="222" r="40" fill="#fff"/>
    <circle cx="600" cy="222" r="20" fill="var(--blue)"/>
  </svg>
</section>

<section class="section services">
  <p class="eyebrow center">Our Services</p>
  <h2 class="heading center">Care That Meets <b>You Where You Are</b></h2>
  <div class="card-row">
    <article class="svc-card">
      <div class="icon-circ"><svg width="36" height="36" viewBox="0 0 36 36" fill="none" stroke="#222" stroke-width="1.5"><path d="M6 24h24M9 24l3-8h12l3 8M18 6v10"/></svg></div>
      <h3>HIV Treatment</h3>
      <p>Expert HIV care, medication management, and ongoing support through secure telehealth appointments with a provider who knows your history.</p>
      <a class="more" href="#">Book HIV care <svg width="18" height="10" viewBox="0 0 18 10"><path d="M0 5h16M12 1l4 4-4 4" stroke="currentColor" stroke-width="1.6" fill="none"/></svg></a>
    </article>
    <article class="svc-card featured">
      <div class="icon-circ"><svg width="36" height="36" viewBox="0 0 36 36" fill="none" stroke="#222" stroke-width="1.5"><path d="M5 12c6-4 20-4 26 0-2 8-8 14-16 14-4 0-8-6-10-14z"/></svg></div>
      <h3>Hepatitis C</h3>
      <p>Diagnosis, treatment planning, and follow-up care to help you achieve better health — with clear next steps at every appointment.</p>
      <a class="more" href="#">Book Hep C care <svg width="18" height="10" viewBox="0 0 18 10"><path d="M0 5h16M12 1l4 4-4 4" stroke="currentColor" stroke-width="1.6" fill="none"/></svg></a>
    </article>
    <article class="svc-card">
      <div class="icon-circ"><svg width="36" height="36" viewBox="0 0 36 36" fill="none" stroke="#222" stroke-width="1.5"><rect x="14" y="5" width="8" height="26" rx="3"/><path d="M14 14h8"/></svg></div>
      <h3>HIV Treatment</h3>
      <p>Protect yourself from HIV with confidential online PrEP consultations and prescriptions, tailored to your risk profile and lifestyle.</p>
      <a class="more" href="#">Book HIV care <svg width="18" height="10" viewBox="0 0 18 10"><path d="M0 5h16M12 1l4 4-4 4" stroke="currentColor" stroke-width="1.6" fill="none"/></svg></a>
    </article>
  </div>
</section>

<section class="section why">
  <div class="why-art" role="img" aria-label="Provider wearing a headset on a video consultation with patients on a laptop"></div>
  <p class="eyebrow">Why Choose BRV Online</p>
  <h2 class="heading">Compassionate Care.<br><b>Modern Convenience</b></h2>
  <ul class="checks">
    <li><svg width="18" height="18" viewBox="0 0 18 18" fill="none" stroke="#222" stroke-width="1.4"><circle cx="9" cy="9" r="8"/><path d="M5 9l3 3 5-6"/></svg>Private &amp; Confidential</li>
    <li><svg width="18" height="18" viewBox="0 0 18 18" fill="none" stroke="#222" stroke-width="1.4"><circle cx="9" cy="9" r="8"/><path d="M5 9l3 3 5-6"/></svg>Telemedicine Convenience</li>
    <li><svg width="18" height="18" viewBox="0 0 18 18" fill="none" stroke="#222" stroke-width="1.4"><circle cx="9" cy="9" r="8"/><path d="M5 9l3 3 5-6"/></svg>Experienced Healthcare Providers</li>
    <li><svg width="18" height="18" viewBox="0 0 18 18" fill="none" stroke="#222" stroke-width="1.4"><circle cx="9" cy="9" r="8"/><path d="M5 9l3 3 5-6"/></svg>Secure Online Consultations</li>
    <li><svg width="18" height="18" viewBox="0 0 18 18" fill="none" stroke="#222" stroke-width="1.4"><circle cx="9" cy="9" r="8"/><path d="M5 9l3 3 5-6"/></svg>Fast Appointment Scheduling</li>
    <li><svg width="18" height="18" viewBox="0 0 18 18" fill="none" stroke="#222" stroke-width="1.4"><circle cx="9" cy="9" r="8"/><path d="M5 9l3 3 5-6"/></svg>Personalized Treatment Plans</li>
  </ul>
</section>

<section class="section steps">
  <p class="eyebrow center">How It Works</p>
  <h2 class="heading center">Simples Steps <b>to Better Health</b></h2>
  <div class="step-row">
    <article class="step"><span class="num">01</span>
      <div class="icon-circ"><svg width="34" height="34" viewBox="0 0 34 34" fill="none" stroke="#222" stroke-width="1.5"><rect x="6" y="7" width="22" height="16" rx="2"/><path d="M3 27h28"/></svg></div>
      <h3>Book Online</h3><p>Choose a time that works for you in under two minutes — no referral needed.</p></article>
    <article class="step"><span class="num">02</span>
      <div class="icon-circ"><svg width="34" height="34" viewBox="0 0 34 34" fill="none" stroke="#222" stroke-width="1.5"><circle cx="11" cy="11" r="4"/><circle cx="23" cy="11" r="4"/><path d="M4 27c1-6 13-6 14 0M16 27c1-6 13-6 14 0"/></svg></div>
      <h3>Meet Your Provider</h3><p>Join a secure video visit and talk through your health history and goals.</p></article>
    <article class="step"><span class="num">03</span>
      <div class="icon-circ"><svg width="34" height="34" viewBox="0 0 34 34" fill="none" stroke="#222" stroke-width="1.5"><rect x="8" y="10" width="12" height="18" rx="2"/><path d="M10 6h8v4h-8zM22 16l6 6"/></svg></div>
      <h3>Receive Your Treatment Plan</h3><p>Get a plan and prescriptions sent to your pharmacy of choice, same day.</p></article>
    <article class="step"><span class="num">04</span>
      <div class="icon-circ"><svg width="34" height="34" viewBox="0 0 34 34" fill="none" stroke="#222" stroke-width="1.5"><circle cx="17" cy="17" r="11"/><circle cx="17" cy="17" r="5"/></svg></div>
      <h3>Ongoing Support</h3><p>Message your care team and schedule follow-ups whenever you need to.</p></article>
  </div>
</section>

<section class="section stories">
  <p class="eyebrow center">Patient Stories</p>
  <h2 class="heading center">Care People Trust With <b>Something<br>Personal</b></h2>
  <div class="story-row">
    <article class="story"><div class="stars">★★★★★</div>
      <q>"Fantastic service and incredible selection. Exactly what collectors are looking for."</q>
      <div class="person"><span class="avatar" role="img" aria-label="Patient portrait"></span><div><strong>M., PrEP patient</strong><small>Member since 2025</small></div></div></article>
    <article class="story"><div class="stars">★★★★★</div>
      <q>"Fantastic service and incredible selection. Exactly what collectors are looking for."</q>
      <div class="person"><span class="avatar" role="img" aria-label="Patient portrait"></span><div><strong>J., HIV treatment patient</strong><small>Member since 2025</small></div></div></article>
    <article class="story"><div class="stars">★★★★★</div>
      <q>"Fantastic service and incredible selection. Exactly what collectors are looking for."</q>
      <div class="person"><span class="avatar" role="img" aria-label="Patient portrait"></span><div><strong>Hepatitis C patient</strong><small>Member since 2025</small></div></div></article>
  </div>
</section>

<section class="section cta">
  <p class="eyebrow center">Ready When You Are</p>
  <h2 class="heading center">Take Control Of <b>Your Health<br>Today</b></h2>
  <p class="center">Book Your Confidential Online Appointment And Hear Back From A Provider Within Days.</p>
  <a class="btn btn-grad" href="#">Book Now</a>
  <svg class="footer-curve" width="1200" height="180" viewBox="0 0 1200 180">
    <path d="M0 180 Q300 20 600 40 Q900 20 1200 180Z" fill="var(--navy)"/>
    <path d="M110 115 Q380 10 600 20 Q820 10 1090 115 Q820 40 600 45 Q380 40 110 115Z" fill="var(--green)"/>
    <circle cx="600" cy="40" r="40" fill="#fff"/>
    <circle cx="600" cy="40" r="20" fill="var(--blue)"/>
  </svg>
</section>

<footer class="section site-footer">
  <div class="foot-brand"><span class="brand-dot"></span>BRV Online</div>
  <div class="foot-col" style="left:432px">
    <h4>QUICK LINKS</h4>
    <ul>
      <li><span class="dot-tick"><svg width="9" height="9" viewBox="0 0 9 9"><path d="M1 5l2 2 5-5" stroke="#fff" stroke-width="1.5" fill="none"/></svg></span>Home</li>
      <li><span class="dot-tick"><svg width="9" height="9" viewBox="0 0 9 9"><path d="M1 5l2 2 5-5" stroke="#fff" stroke-width="1.5" fill="none"/></svg></span>PrEP</li>
      <li><span class="dot-tick"><svg width="9" height="9" viewBox="0 0 9 9"><path d="M1 5l2 2 5-5" stroke="#fff" stroke-width="1.5" fill="none"/></svg></span>HIV Treatment</li>
      <li><span class="dot-tick"><svg width="9" height="9" viewBox="0 0 9 9"><path d="M1 5l2 2 5-5" stroke="#fff" stroke-width="1.5" fill="none"/></svg></span>Hep C</li>
      <li><span class="dot-tick"><svg width="9" height="9" viewBox="0 0 9 9"><path d="M1 5l2 2 5-5" stroke="#fff" stroke-width="1.5" fill="none"/></svg></span>Contact Us</li>
    </ul>
  </div>
  <div class="foot-col" style="left:612px">
    <h4>HELP LINKS</h4>
    <ul>
      <li><span class="dot-tick"><svg width="9" height="9" viewBox="0 0 9 9"><path d="M1 5l2 2 5-5" stroke="#fff" stroke-width="1.5" fill="none"/></svg></span>Home</li>
      <li><span class="dot-tick"><svg width="9" height="9" viewBox="0 0 9 9"><path d="M1 5l2 2 5-5" stroke="#fff" stroke-width="1.5" fill="none"/></svg></span>How it works</li>
      <li><span class="dot-tick"><svg width="9" height="9" viewBox="0 0 9 9"><path d="M1 5l2 2 5-5" stroke="#fff" stroke-width="1.5" fill="none"/></svg></span>Contact us</li>
    </ul>
  </div>
  <div class="foot-col" style="left:850px">
    <h4>GET IN TOUCH</h4>
    <ul>
      <li><svg width="16" height="16" viewBox="0 0 16 16"><path d="M3 1l3 3-2 2c1 2 3 4 5 5l2-2 3 3-2 3C6 14 2 10 1 3z" fill="var(--green)"/></svg>+1 555-010-2040</li>
      <li><svg width="16" height="16" viewBox="0 0 16 16"><circle cx="8" cy="8" r="7" fill="var(--green)"/><path d="M4 6h8v5H4zM4 6l4 3 4-3" stroke="#fff" fill="none"/></svg>care@brvonline.example</li>
      <li><svg width="16" height="16" viewBox="0 0 16 16" fill="none" stroke="var(--green)" stroke-width="1.4"><circle cx="8" cy="8" r="7"/><path d="M1 8h14M8 1c3 3 3 11 0 14M8 1c-3 3-3 11 0 14"/></svg>www.brvonline.example</li>
    </ul>
  </div>
  <div class="foot-rule"></div>
  <p class="copyright">Copyright 2026. Company Name. All Rights Reserved</p>
</footer>

</body>
</html>
```